A4 Single Sided Brochure Folder Design Technical Company

We are a technical company based in the UK, working worldwide for Power Distribution companies.

We have technical literature and need a folder to present these in. The design should be very simple and clean using our logo and "Innovative Utility Solutions"

Our website brenvox.com gives and idea of the business but don't follow the look of the website as we will be redoing shortly.

Requirements
Must have
• Logo and Strap Line
Nice to have
• Clean, easy to print and timeless
Should not have
• Shouldn't be fashionable, we certainly aren't

```html
<!DOCTYPE html>
<html lang="en">
<head>
<meta charset="utf-8">
<title>Brenvox Folder</title>
<link href="https://fonts.googleapis.com/css2?family=Roboto:wght@300;400;500;700&display=swap" rel="stylesheet">
<style>
  :root {
    --magenta: #c42a8f;
    --magenta-soft: rgba(214, 70, 160, 0.82);
    --cyan: #12a7e6;
    --ink: #1c1c1c;
    --paper: #f6f6f6;
    --green: #3bad45;
    --backdrop: #2d2d2d;
  }
  * { margin: 0; padding: 0; box-sizing: border-box; }
  html, body { width: 1200px; height: 1200px; overflow: hidden; }
  body { background: var(--backdrop); font-family: "Roboto", sans-serif; position: relative; }

  .page { position: absolute; top: 226px; width: 530px; height: 750px; background: var(--paper); overflow: hidden; }
  .page--front { left: 40px; }
  .page--back { left: 632px; background: #fff; }
  .band { position: absolute; left: 0; width: 100%; background: var(--magenta); }
  .photo { position: absolute; }

  /* Front */
  .front-header { top: 0; height: 83px; display: flex; align-items: center; justify-content: center; }
  .brand-name { color: #fff; font-weight: 300; font-size: 26px; letter-spacing: 0.5px; font-family: "Roboto", sans-serif; }
  .front-title { position: absolute; top: 96px; width: 100%; text-align: center; }
  .front-title__line1 { font-size: 29px; font-weight: 500; color: var(--ink); line-height: 1.1; }
  .front-title__line2 { font-size: 50px; font-weight: 700; color: var(--cyan); line-height: 1; letter-spacing: 1px; }
  .front-strip-top { top: 184px; height: 11px; }
  .front-photo { left: 0; top: 195px; width: 530px; height: 365px; background: linear-gradient(160deg, #e9e9ee 0%, #d4d5db 55%, #b9bbc2 100%); }
  .front-strip-mid { top: 572px; height: 10px; }
  .quote { position: absolute; top: 602px; left: 80px; width: 370px; text-align: center; font-size: 12.3px; color: var(--ink); line-height: 1.25; }
  .quote-mark { position: absolute; color: var(--magenta); font-weight: 700; font-size: 52px; line-height: 1; }
  .quote-mark--open { left: 46px; top: 590px; }
  .quote-mark--close { left: 462px; top: 628px; }
  .quote-rule { position: absolute; left: 88px; top: 650px; width: 352px; height: 1px; background: #e2e2e2; }
  .site-bar { position: absolute; left: 164px; top: 691px; width: 200px; height: 16px; background: var(--green); color: var(--magenta); font-size: 12px; text-align: center; line-height: 16px; }
  .front-footer { bottom: 0; height: 18px; }

  /* Back */
  .back-header { top: 0; height: 31px; }
  .back-photo--pylons { left: 0; top: 54px; width: 250px; height: 292px; background: linear-gradient(180deg, #c9ccd2 0%, #a79f8e 55%, #6c5d52 100%); }
  .back-photo--valley { left: 264px; top: 31px; width: 233px; height: 223px; background: linear-gradient(180deg, #8fb9e3 0%, #5d8a3a 45%, #557a2e 80%, #9aa6a0 100%); }
  .back-photo--panel { left: 0; top: 356px; width: 250px; height: 123px; background: linear-gradient(160deg, #e6e6ea 0%, #c3c4ca 100%); }
  .back-photo--tanks { left: 264px; top: 267px; width: 266px; height: 212px; background: linear-gradient(170deg, #a8ad9a 0%, #e8e8e6 45%, #7f8a6e 100%); }
  .strapline-pill { position: absolute; left: 62px; top: 245px; width: 406px; height: 55px; border-radius: 22px; background: var(--magenta-soft); color: #fff; font-size: 19px; font-weight: 500; display: flex; align-items: center; justify-content: center; letter-spacing: 0.3px; }
  .back-footer { top: 493px; height: 257px; color: #fff; }
  .info-heading { position: absolute; top: 22px; font-size: 14px; font-weight: 500; letter-spacing: 0.3px; }
  .info-rule { position: absolute; top: 52px; height: 2px; background: rgba(255,255,255,0.85); }
  .about { left: 40px; }
  .about-text { position: absolute; left: 40px; top: 66px; width: 150px; font-size: 8.6px; line-height: 12.4px; text-align: justify; }
  .contact { left: 353px; }
  .contact-text { position: absolute; left: 353px; top: 66px; font-size: 8.6px; line-height: 12.4px; }
  .contact-text p + p { margin-top: 5px; }
  .back-brand { position: absolute; left: 220px; top: 74px; font-size: 24px; font-weight: 300; color: #fff; }
</style>
</head>
<body>

  <section class="page page--front">
    <div class="band front-header"><span class="brand-name">Brenvox</span></div>
    <h1 class="front-title">
      <div class="front-title__line1">INNOVATIVE UTILITY</div>
      <div class="front-title__line2">SOLUTIONS</div>
    </h1>
    <div class="band front-strip-top"></div>
    <div class="photo front-photo" role="img" aria-label="Close-up of a white instrument panel with flow meters, gauges, valves and red tubing"></div>
    <div class="band front-strip-mid"></div>
    <span class="quote-mark quote-mark--open">&ldquo;</span>
    <p class="quote">Brenvox Limited is an independent company providing specialist services to the utility, oil and gas and infrastructure sectors, worldwide.</p>
    <div class="quote-rule"></div>
    <span class="quote-mark quote-mark--close">&rdquo;</span>
    <div class="site-bar">www.brenvox.com</div>
    <div class="band front-footer"></div>
  </section>

  <section class="page page--back">
    <div class="band back-header"></div>
    <div class="photo back-photo--pylons" role="img" aria-label="Electrical substation with concrete gantries and insulators"></div>
    <div class="photo back-photo--valley" role="img" aria-label="Green wooded hillside above a lake under blue sky"></div>
    <div class="photo back-photo--panel" role="img" aria-label="Instrument panel with gauges and tubing"></div>
    <div class="photo back-photo--tanks" role="img" aria-label="Aerial view of white storage tanks on grass"></div>
    <div class="strapline-pill">INNOVATIVE UTILITY SOLUTIONS</div>

    <div class="band back-footer">
      <h2 class="info-heading about">ABOUT BRENVOX</h2>
      <div class="info-rule about" style="width:150px"></div>
      <p class="about-text">Brenvox first began working with fluid filled cables in 2007 with our first successful PFT tracer location later that year. Our cross sector experience ranging from utility, engineering, petrochemical and environmental industries gives us a unique perspective from which to provide innovative solutions.</p>

      <span class="back-brand">Brenvox</span>

      <h2 class="info-heading contact">CONTACT</h2>
      <div class="info-rule contact" style="width:126px"></div>
      <div class="contact-text">
        <p>Registered Office<br>Alder Court<br>Off Meadow Lane<br>Ashbridge<br>AB1 2CD<br>United Kingdom</p>
        <p>Phone UK and ROW: +441632 960418<br>Fax: +441632960527<br>South East UK: +441632 960733</p>
        <p style="margin-top:12px">Email: info@brenvox.com</p>
      </div>
    </div>
  </section>

</body>
</html>
```